SkyvoraQ Business Cards and Stationary Design

Need a design for our business cards and stationary. I want to carry on the theme of the logo. I want the business cards to have a design on the back. I would like the business cards and the stationary to carry the same theme, design scheme, and branding

Target Market(s)

Airlines and Maintenance Facilities

Industry/Entity Type

Aviation

Contact Information for Business Card

Name
Position Title
Address: 4827 Tollbeck Lane, Fort Pierce, Florida, 34951
Office Number
Mobile Number
Email
Website

Font styles to use
Serif
Sans Serif

Colors

Designer to choose colors to be used in the design.

```html
<!DOCTYPE html>
<html lang="en">
<head>
<meta charset="utf-8">
<title>SkyvoraQ Business Card</title>
<link href="https://fonts.googleapis.com/css2?family=Montserrat:wght@600;700&family=Open+Sans:wght@300;400&display=swap" rel="stylesheet">
<style>
  :root {
    --backdrop: #e8e2db;
    --card: #f3f2f0;
    --card-edge: #dcdad6;
    --navy: #2e3a56;
    --slate: #4c5b7c;
    --grey: #6f6f72;
    --soft-grey: #8a8a8d;
    --blue: #1f88c0;
    --blue-deep: #1b5a98;
  }
  html, body {
    margin: 0;
    padding: 0;
    width: 1200px;
    height: 1047px;
    overflow: hidden;
    background: var(--backdrop);
  }
  .business-card {
    position: absolute;
    left: 125px;
    top: 267px;
    width: 950px;
    height: 512px;
    background: var(--card);
    border: 1px solid var(--card-edge);
    border-radius: 22px;
    overflow: hidden;
    box-shadow: 0 6px 24px rgba(60, 50, 40, 0.12);
    font-family: "Open Sans", Arial, sans-serif;
  }
  .brand-dot {
    position: absolute;
    left: 150px;
    top: 26px;
    width: 70px;
    height: 70px;
    border-radius: 50%;
    background: var(--blue);
  }
  .brand-name {
    position: absolute;
    left: 65px;
    top: 106px;
    margin: 0;
    font-family: "Montserrat", Arial, sans-serif;
    font-weight: 700;
    font-size: 25px;
    letter-spacing: 3px;
    text-transform: uppercase;
    color: var(--navy);
  }
  .person {
    position: absolute;
    left: 65px;
    top: 176px;
  }
  .person-name {
    margin: 0;
    font-family: "Montserrat", Arial, sans-serif;
    font-weight: 700;
    font-size: 30px;
    letter-spacing: 1px;
    text-transform: uppercase;
    color: var(--slate);
    line-height: 1.1;
  }
  .person-title {
    margin: 2px 0 0;
    font-size: 21px;
    color: var(--grey);
  }
  .contact-list {
    position: absolute;
    left: 65px;
    top: 270px;
    margin: 0;
    padding: 0;
    list-style: none;
  }
  .contact-item {
    display: flex;
    align-items: center;
    height: 32px;
    font-weight: 300;
    font-size: 21px;
    color: var(--soft-grey);
  }
  .contact-item svg {
    width: 18px;
    height: 18px;
    margin-right: 23px;
    flex: none;
  }
  .contact-item .accent { color: var(--blue); }
  .address {
    position: absolute;
    left: 65px;
    top: 420px;
    margin: 0;
    font-style: normal;
    font-size: 21px;
    line-height: 27px;
    color: var(--grey);
  }
  .brand-backdrop {
    position: absolute;
    left: 500px;
    top: -20px;
    width: 560px;
    height: 560px;
  }
</style>
</head>
<body>
  <div class="business-card">
    <svg class="brand-backdrop" viewBox="0 0 560 560" aria-hidden="true">
      <defs>
        <linearGradient id="brand-fill" x1="0" y1="0" x2="1" y2="1">
          <stop offset="0" stop-color="#1f93c6"/>
          <stop offset="1" stop-color="#1b4f8f"/>
        </linearGradient>
      </defs>
      <circle cx="290" cy="290" r="270" fill="url(#brand-fill)" opacity="0.9"/>
    </svg>

    <div class="brand-dot" aria-hidden="true"></div>
    <p class="brand-name">SkyvoraQ</p>

    <div class="person">
      <p class="person-name">Daniel Revick</p>
      <p class="person-title">Vice President</p>
    </div>

    <ul class="contact-list">
      <li class="contact-item">
        <svg viewBox="0 0 24 24" aria-hidden="true"><path fill="#2e5a8f" d="M6.6 3.5l3 3.2-1.7 2.3c1.2 2.5 3.2 4.6 5.8 5.9l2.3-1.7 3.2 3-1.7 3.2C11 18.7 5.3 13 4 5.2z"/></svg>
        503 417 2286
      </li>
      <li class="contact-item">
        <svg viewBox="0 0 24 24" aria-hidden="true"><rect x="6" y="2" width="12" height="20" rx="2" fill="none" stroke="#2e5a8f" stroke-width="2.4"/><circle cx="12" cy="18" r="1.3" fill="#2e5a8f"/></svg>
        503 465 9071
      </li>
      <li class="contact-item">
        <svg viewBox="0 0 24 24" aria-hidden="true"><rect x="3" y="5.5" width="18" height="13" rx="1.5" fill="none" stroke="#2e5a8f" stroke-width="2.2"/><path d="M3.5 6.5l8.5 6.5 8.5-6.5" fill="none" stroke="#2e5a8f" stroke-width="2.2"/></svg>
        info@skyvoraq.com
      </li>
      <li class="contact-item">
        <svg viewBox="0 0 24 24" aria-hidden="true"><g fill="none" stroke="#2e5a8f" stroke-width="1.8"><circle cx="12" cy="12" r="9"/><ellipse cx="12" cy="12" rx="4" ry="9"/><path d="M3 12h18M5 7h14M5 17h14"/></g></svg>
        <span>www.<span class="accent">skyvoraq</span>.com</span>
      </li>
    </ul>

    <address class="address">4827 Tollbeck Lane<br>Fort Pierce, Florida, 34951</address>
  </div>
</body>
</html>
```